International oil and gas consultancy needs a business card design

We need a business card design for a new oil and gas consultancy business based in Perth Australia. This is a professional services business and needs a moderately conservative type of business card. The business card also needs to be simple and uncluttered. The colour of the business logo is dark red (see attached file).
The front of the card should have a white background and mainly black lettering and perhaps some use of dark red and/or grey (your choice).
The back of the card should have a light grey background with dark red, black and or both dark red & black lettering (your choice).
Please find attached a clear brief of how I would like the business card designed.
Updates

Hello Everyone, I have slightly modified the brief. The main change is to incorporate some dark red and grey colours into the card, while still keeping the black lettering dominant. I have made the changes in the attached detailed brief document. Regards

Please note, the front of the card must say Harbor Ledger Advisory (in addition to the logo).

Industry/Entity Type

Conservative

Requirements
Must have
• brief has been updated. please refer to attachment for details.

Front of the card MUST say Harbor Ledger Advisory (in addition to the logo)

```html
<!DOCTYPE html>
<html lang="en">
<head>
<meta charset="utf-8">
<title>Harbor Ledger Advisory – Business Card</title>
<link rel="stylesheet" href="https://fonts.googleapis.com/css2?family=Open+Sans:wght@400;600;700&display=swap">
<style>
  :root {
    --backdrop: #8d8f90;
    --card-front: #ffffff;
    --card-back: #e6e6e6;
    --brand-red: #9b1c22;
    --band-line: #ffffff;
    --ink: #1c1c1c;
    --ink-soft: #333333;
    --icon: #3a3a3a;
  }
  * { box-sizing: border-box; margin: 0; padding: 0; }
  html, body { width: 1200px; height: 772px; overflow: hidden; }
  body {
    background: var(--backdrop);
    font-family: "Open Sans", Arial, sans-serif;
    position: relative;
  }
  .card {
    position: absolute;
    top: 238px;
    width: 520px;
    height: 296px;
    box-shadow: 0 6px 18px rgba(0,0,0,0.25);
    overflow: hidden;
  }
  .card--back { left: 60px; background: var(--card-back); }
  .card--front { left: 620px; background: var(--card-front); }

  .brand {
    display: flex;
    align-items: center;
    white-space: nowrap;
  }
  .brand__mark {
    flex: none;
    background: var(--brand-red);
  }
  .brand__name {
    color: var(--ink);
    font-weight: 700;
  }

  .card--back .brand {
    position: absolute;
    left: 0; right: 0;
    top: 126px;
    justify-content: center;
    gap: 14px;
  }
  .card--back .brand__mark { width: 36px; height: 36px; }
  .card--back .brand__name { font-size: 29px; }

  .card--front .brand {
    position: absolute;
    right: 34px;
    top: 56px;
    gap: 10px;
  }
  .card--front .brand__mark { width: 26px; height: 26px; }
  .card--front .brand__name { font-size: 23px; }

  .name-band {
    position: absolute;
    left: 0; right: 0;
    top: 124px;
    height: 46px;
    background: var(--brand-red);
  }
  .name-band::before, .name-band::after {
    content: "";
    position: absolute;
    left: 0; right: 0;
    height: 1px;
    background: var(--band-line);
  }
  .name-band::before { top: 5px; }
  .name-band::after { bottom: 5px; }
  .name-band__text {
    position: absolute;
    right: 34px;
    top: 0;
    line-height: 46px;
    color: #fff;
    font-size: 15px;
    font-weight: 600;
  }
  .name-band__role { font-weight: 400; }

  .contact-list {
    position: absolute;
    left: 26px;
    right: 20px;
    top: 196px;
    list-style: none;
    display: grid;
    grid-template-columns: auto auto auto;
    justify-content: space-between;
    row-gap: 12px;
    font-size: 11px;
    color: var(--ink-soft);
  }
  .contact-item { display: flex; align-items: center; gap: 5px; white-space: nowrap; }
  .contact-item svg { width: 12px; height: 12px; flex: none; }
</style>
</head>
<body>

  <section class="card card--back" aria-label="Card back">
    <div class="brand">
      <span class="brand__mark" aria-hidden="true"></span>
      <p class="brand__name">Harbor Ledger Advisory</p>
    </div>
  </section>

  <section class="card card--front" aria-label="Card front">
    <div class="brand">
      <span class="brand__mark" aria-hidden="true"></span>
      <p class="brand__name">Harbor Ledger Advisory</p>
    </div>

    <div class="name-band">
      <p class="name-band__text">Daniel Reeve | <span class="name-band__role">Owner / CEO</span></p>
    </div>

    <ul class="contact-list">
      <li class="contact-item">
        <svg viewBox="0 0 12 12" aria-hidden="true"><circle cx="6" cy="6" r="6" fill="var(--icon)"/><path d="M4 3.2l1 1.3-.6.7c.4.9 1 1.5 1.9 1.9l.7-.6 1.3 1-.6 1.1C5.6 8.5 3.5 6.4 3.4 4z" fill="#fff"/></svg>
        208-555-0143
      </li>
      <li class="contact-item">
        <svg viewBox="0 0 12 12" aria-hidden="true"><circle cx="6" cy="6" r="6" fill="var(--icon)"/><path d="M6 2.6a2.2 2.2 0 0 0-2.2 2.2C3.8 6.5 6 9.4 6 9.4s2.2-2.9 2.2-4.6A2.2 2.2 0 0 0 6 2.6z" fill="#fff"/><circle cx="6" cy="4.8" r=".8" fill="var(--icon)"/></svg>
        Suite 4, Quay House, Perth WA 6000
      </li>
      <li class="contact-item">
        <svg viewBox="0 0 12 12" aria-hidden="true"><circle cx="6" cy="6" r="6" fill="var(--icon)"/><circle cx="6" cy="6" r="3.2" fill="none" stroke="#fff" stroke-width=".8"/><path d="M2.8 6h6.4M6 2.8c-1.5 1.8-1.5 4.6 0 6.4M6 2.8c1.5 1.8 1.5 4.6 0 6.4" fill="none" stroke="#fff" stroke-width=".7"/></svg>
        www.harborledger.com
      </li>
      <li class="contact-item">
        <svg viewBox="0 0 12 12" aria-hidden="true"><circle cx="6" cy="6" r="6" fill="var(--icon)"/><path d="M4 3.2l1 1.3-.6.7c.4.9 1 1.5 1.9 1.9l.7-.6 1.3 1-.6 1.1C5.6 8.5 3.5 6.4 3.4 4z" fill="#fff"/></svg>
        208-555-0178
      </li>
      <li class="contact-item">
        <svg viewBox="0 0 12 12" aria-hidden="true"><circle cx="6" cy="6" r="6" fill="var(--icon)"/><rect x="3.8" y="2.8" width="4.4" height="6.4" rx=".6" fill="#fff"/><rect x="4.5" y="3.6" width="3" height="4" fill="var(--icon)"/></svg>
        208-555-0192
      </li>
      <li class="contact-item">
        <svg viewBox="0 0 12 12" aria-hidden="true"><circle cx="6" cy="6" r="6" fill="var(--icon)"/><rect x="3" y="3.8" width="6" height="4.4" fill="#fff"/><path d="M3 3.8l3 2.4 3-2.4" fill="none" stroke="var(--icon)" stroke-width=".7"/></svg>
        daniel@harborledger.com
      </li>
    </ul>
  </section>

</body>
</html>
```